Web Design Project - Investor Services

I would like a simple and elegant web design for my company "Corvalo Management". The company will provide services to Corporate and Institutional investors for their needs with local/foreign investment vehicles. The website will have four pages to start: home, about us, services, contact.
I already chose a logo, and I will attach the source file. The color that I will most probably use for the logo will be blue, and i also like grey with a white background. For the website I would like to see light colors, maybe light green or grey, with the logo either in blue, grey or white (depeding on the background).
Target Market(s)
Investment managers and tax/legal advisors from top firms. This is the reason why I want something simple and elegant.
Industry/Entity Type
Investment
Requirements
Nice to have
- I do not want many pictures in the website, but I might include a couple of pictures of Madrid and maybe a picture of myself in the about us page (still deciding). I will attach some pictures of Madrid that I like, but feel free to search for others - i have others but i am not able to attach all of them.

```html
<!DOCTYPE html>
<html lang="en">
<head>
<meta charset="utf-8">
<title>Corvalo Management</title>
<link href="https://fonts.googleapis.com/css2?family=Source+Sans+3:wght@300;400;600&display=swap" rel="stylesheet">
<style>
:root{
  --purple:#5a2387;
  --purple-deep:#4d1870;
  --purple-bright:#6e2e9e;
  --purple-soft:#c7a6e3;
  --nav-ink:#4a2a78;
  --ink:#3a3a3a;
  --ink-soft:#6b6b6b;
  --line:#d9d9d9;
  --footer-bg:#f4f3f4;
  --white:#ffffff;
}
*{box-sizing:border-box;margin:0;padding:0}
html,body{width:1200px;height:1045px;overflow:hidden}
body{
  position:relative;
  font-family:"Source Sans 3",Arial,sans-serif;
  color:var(--ink);
  background:linear-gradient(180deg,#ffffff 0,#f9f8fa 300px,#efedf0 420px,#ffffff 421px);
}
.top-rule{position:absolute;left:0;top:0;width:1200px;height:3px;background:#ebe9f1}
.brand{
  position:absolute;left:78px;top:46px;
  font-weight:300;font-size:40px;letter-spacing:.5px;color:var(--purple-bright);
}
.main-nav{position:absolute;right:80px;top:57px;display:flex;height:65px}
.main-nav a{
  display:block;padding:20px 19px 0;font-size:20px;font-weight:300;
  color:var(--nav-ink);text-decoration:none;border-left:1px solid var(--line);
}
.main-nav a:first-child{border-left:none}
.hero{
  position:absolute;left:68px;top:123px;width:1066px;height:421px;
  background:var(--white);border:1px solid #e2e2e2;border-radius:3px;
  box-shadow:0 1px 4px rgba(0,0,0,.08);
}
.hero-photo{
  position:absolute;left:8px;top:8px;width:731px;height:405px;border-radius:3px 0 0 3px;
  background:linear-gradient(180deg,#5f6070 0%,#9a8a97 20%,#d9a3a1 45%,#e1a9a4 62%,#7a5f63 78%,#151214 100%);
}
.hero-panel{
  position:absolute;left:739px;top:8px;width:318px;height:405px;border-radius:0 3px 3px 0;
  background:linear-gradient(180deg,#6a2d9b 0%,#5a2188 55%,#4b1569 100%);
  border-left:5px solid #8b4fc0;
  padding:58px 24px 0 32px;color:var(--white);
}
.hero-kicker{font-size:20px;font-weight:300;color:var(--purple-soft);line-height:24px}
.hero-title{font-size:26px;font-weight:400;line-height:30px;margin-top:4px;margin-left:-2px}
.hero-text{font-size:12.5px;font-weight:300;line-height:22.5px;margin-top:10px}
.hero-dots{display:flex;gap:4px;margin-top:20px;margin-left:4px}
.hero-dots span{width:12px;height:12px;border-radius:50%;background:#8c5bbb}
.hero-dots span.is-active{background:var(--white)}
.column{position:absolute;top:596px}
.column h2{font-size:25px;font-weight:300;color:#2f2f2f;line-height:30px}
.column h2 strong{font-weight:600}
.col-about{left:75px;width:313px}
.col-services{left:459px;width:285px}
.col-invest{left:795px;width:320px}
.divider{position:absolute;top:600px;width:1px;height:252px;background:var(--line)}
.lead{font-size:13.5px;font-weight:600;line-height:25.5px;margin-top:12px;color:#2f2f2f;text-align:justify}
.body-copy{font-size:13.5px;font-weight:300;line-height:25.5px;color:var(--ink-soft);margin-top:6px;text-align:justify}
.col-services .body-copy{margin-top:12px;text-align:left}
.service-list{list-style:none;margin-top:11px;margin-left:12px}
.service-list li{
  position:relative;padding-left:16px;font-size:13.5px;color:var(--nav-ink);
  line-height:30.5px;text-transform:uppercase;
}
.service-list li::before{
  content:"";position:absolute;left:0;top:10px;
  border-left:6px solid var(--nav-ink);border-top:5px solid transparent;border-bottom:5px solid transparent;
}
.street-photo{
  width:316px;height:133px;margin-top:13px;
  background:linear-gradient(180deg,#8fb0e0 0%,#b8c3d2 30%,#c9c2b6 60%,#8f8a84 100%);
}
.col-invest .lead{margin-top:10px;margin-left:4px}
.col-invest .body-copy{margin-top:0;margin-left:4px;text-align:left}
.site-footer{
  position:absolute;left:0;top:937px;width:1200px;height:108px;
  background:var(--footer-bg);border-top:1px solid #e3e3e3;
}
.social{position:absolute;left:86px;top:26px;display:flex;gap:6px}
.social span{width:20px;height:20px;border-radius:50%;background:#555}
.footer-nav{position:absolute;left:171px;top:28px;font-size:14px;color:#555}
.footer-nav a{color:#555;text-decoration:none}
.footer-nav .sep{margin:0 8px}
.copyright{position:absolute;right:80px;top:30px;font-size:12.5px;color:#666}
</style>
</head>
<body>
<div class="top-rule"></div>

<header>
  <div class="brand">Corvalo Management</div>
  <nav class="main-nav">
    <a href="#">Home</a>
    <a href="#">About us</a>
    <a href="#">Services</a>
    <a href="#">Contact</a>
  </nav>
</header>

<section class="hero">
  <div class="hero-photo" role="img" aria-label="Madrid business district skyline with towers at dusk"></div>
  <div class="hero-panel">
    <p class="hero-kicker">We Provide Services to</p>
    <h1 class="hero-title">Corporate and Institutional Investors</h1>
    <p class="hero-text">Nunc tempus felis vitae urna. Vivamus porttitor, g, purus nisi eleifend libero, a tempus libero lectus feugiat felis. Morbi diam mauris, viverra in, gravida eu, mattis in, ante. Morbi eget arcu. Morbi porta, libero id</p>
    <div class="hero-dots"><span class="is-active"></span><span></span><span></span></div>
  </div>
</section>

<section class="column col-about">
  <h2><strong>About</strong> Corvalo Management</h2>
  <p class="lead">Nunc tempus felis vitae urna. purus nisi eleifend libero, a tempus libero lectus feugiat felis.</p>
  <p class="body-copy">Morbi eget arcu. Morbi porta, libero id ullamcorper nonummy, nibh ligula pulvinar metus, eget consectetuer augue nisi quis lacus. Ut ac mi quis lacus mollis aliquam. Curabitur iaculis tempus eros. Curabitur vel mi sit amet magna malesuada ultrices. Ut nisi erat, fermentum vel, congue id, euismod in, elit.</p>
</section>
<div class="divider" style="left:428px"></div>

<section class="column col-services">
  <h2><strong>Services</strong> We Provide</h2>
  <p class="body-copy">Vivamus porttitor purus nisi eleifend libero, a tempus libero lectus feugiat felis.</p>
  <ul class="service-list">
    <li>Consectetur adipisicing elit sed</li>
    <li>Do eiusmod tempor</li>
    <li>Incididunt ut labore et dolore</li>
    <li>Minim veniam</li>
    <li>Quis nostrud exercitation</li>
  </ul>
</section>
<div class="divider" style="left:756px"></div>

<section class="column col-invest">
  <h2>Local Foregin Investment</h2>
  <div class="street-photo" role="img" aria-label="Madrid street with historic buildings under a blue sky"></div>
  <p class="lead">Nunc tempus felis vitae urna.</p>
  <p class="body-copy">Vivamus porttitor, g, purus nisi eleifend libero, a tempus libero lectus feugiat felis.</p>
</section>

<footer class="site-footer">
  <div class="social"><span></span><span></span><span></span></div>
  <nav class="footer-nav">
    <a href="#">Home</a><span class="sep">/</span><a href="#">About Us</a><span class="sep">/</span><a href="#">Services</a><span class="sep">/</span><a href="#">Contact</a>
  </nav>
  <p class="copyright">© 2013 Company Name.&nbsp; All right reserved. Term of Use</p>
</footer>
</body>
</html>
```